Business Card - connecting 2 souls and beggining the journey of self discovery

Logo on the front
with tag line

On the back list of services and contact details

Seminars
workshops
Coaching
podcasts

Daniel Porthwick
Health & Wellbeing Life Coach
0491 372 815
daniel@wovenpathwellness.example
wovenpathwellness.example

Industry/Entity Type

Life Coaching

Contact Information for Business Card

I like the use of colour from the logo to be used. I'm not a fan of white.

Requirements
Must have
• My tagline: The journey home starts with you
Nice to have
• Use of colour that is in the Woven Path Wellness logo

```html
<!DOCTYPE html>
<html lang="en">
<head>
<meta charset="utf-8">
<title>Woven Path Wellness – Business Card</title>
<link rel="stylesheet" href="https://fonts.googleapis.com/css2?family=Arimo:wght@400;700&family=Nunito:wght@400;600&display=swap">
<style>
  :root {
    --page: #eef1f1;
    --mint: #72e6cb;
    --mint-light: #b3f4e4;
    --grey-text: #868b8c;
    --green: #33a852;
    --green-light: #3fb45e;
    --purple: #a51fc4;
    --mark: #f0a24a;
  }
  * { box-sizing: border-box; margin: 0; padding: 0; }
  html, body {
    width: 1200px; height: 1200px; overflow: hidden;
    background: var(--page);
  }
  .canvas {
    width: 1200px; height: 1200px;
    display: flex; flex-direction: column; align-items: center; justify-content: center;
    gap: 80px;
  }
  .card {
    position: relative;
    width: 840px; height: 480px;
    background: var(--mint);
    overflow: hidden;
    box-shadow: 0 4px 14px rgba(0,0,0,0.12);
  }
  .card-wave { position: absolute; inset: 0; width: 100%; height: 100%; }
  .card-wave path { fill: var(--mint-light); }

  /* Front */
  .brand {
    position: absolute; left: 230px; top: 80px;
    display: flex; align-items: center; gap: 26px;
  }
  .brand-dot {
    width: 150px; height: 150px; border-radius: 50%;
    background: var(--mark);
  }
  .brand-name {
    font-family: "Nunito", sans-serif; font-weight: 600;
    font-size: 36px; line-height: 1.15; color: var(--purple);
    width: 220px;
  }
  .front-tagline {
    position: absolute; left: 160px; top: 300px;
    font-family: "Nunito", sans-serif; font-weight: 400;
    font-size: 46px; color: var(--grey-text);
  }

  /* Back */
  .coach {
    position: absolute; right: 56px; top: 48px; text-align: right;
    font-family: "Arimo", sans-serif;
  }
  .coach-name { font-weight: 700; font-size: 30px; color: var(--green); }
  .coach-title { font-weight: 400; font-size: 24px; color: var(--green-light); margin-top: 10px; }
  .details {
    position: absolute; left: 250px; top: 190px; width: 420px;
    text-align: center; list-style: none;
    font-family: "Arimo", sans-serif; font-size: 21px; line-height: 1.22;
    color: var(--purple);
  }
  .back-tagline {
    position: absolute; left: 60px; top: 390px;
    font-family: "Arimo", sans-serif; font-weight: 700;
    font-size: 31px; color: var(--green);
  }
</style>
</head>
<body>
<main class="canvas">
  <section class="card card-front" aria-label="Business card front">
    <svg class="card-wave" viewBox="0 0 840 480" preserveAspectRatio="none" aria-hidden="true">
      <path d="M0,480 C180,250 480,40 840,0 C720,250 420,440 0,480 Z"/>
    </svg>
    <div class="brand">
      <span class="brand-dot" aria-hidden="true"></span>
      <span class="brand-name">Woven Path Wellness</span>
    </div>
    <p class="front-tagline">Home of Holistic Health</p>
  </section>

  <section class="card card-back" aria-label="Business card back">
    <svg class="card-wave" viewBox="0 0 840 480" preserveAspectRatio="none" aria-hidden="true">
      <path d="M0,430 C140,180 460,20 840,10 C760,260 420,420 0,470 Z"/>
    </svg>
    <div class="coach">
      <p class="coach-name">Daniel Porthwick</p>
      <p class="coach-title">Health &amp; Wellbeing Life Coach</p>
    </div>
    <ul class="details">
      <li>Seminars,workshops</li>
      <li>Coaching,podcasts</li>
      <li>0491 372 815</li>
      <li>daniel@wovenpathwellness.example</li>
      <li>wovenpathwellness.example</li>
    </ul>
    <p class="back-tagline">The journey home starts with you......</p>
  </section>
</main>
</body>
</html>
```